Business Card cabinets and cabinets components making company.

the card should be formal and interesting at the same time. The main colors will be black and white.

Font styles to use
Sans Serif

Colors

Designer to choose only greyscale colors for use in the design.

Requirements
Must have
• At least must have the followings:
office phone
cell phone
address
position
name
email
web

```html
<!DOCTYPE html>
<html lang="en">
<head>
<meta charset="utf-8">
<title>Plankwell – Business Card</title>
<link href="https://fonts.googleapis.com/css2?family=Oswald:wght@600&family=Work+Sans:wght@400;600&display=swap" rel="stylesheet">
<style>
  :root {
    --backdrop: #161616;
    --card: #1f1f1f;
    --card-sheen: #2a2a2a;
    --ink: #f2f2f2;
    --accent: #b8b8b8;
    --band: #9c9c9c;
  }
  * { box-sizing: border-box; margin: 0; padding: 0; }
  html, body {
    width: 1200px; height: 900px; overflow: hidden;
    background: var(--backdrop);
    font-family: "Work Sans", Arial, sans-serif;
    color: var(--ink);
  }
  .canvas {
    position: relative; width: 1200px; height: 900px;
  }
  .card {
    position: absolute; left: 320px; width: 560px; height: 320px;
    background: linear-gradient(135deg, var(--card) 0%, var(--card) 55%, var(--card-sheen) 100%);
    border-bottom: 6px solid var(--band);
    box-shadow: 0 14px 30px rgba(0,0,0,.55);
  }
  .card--front { top: 95px; }
  .card--back { top: 480px; }

  /* Front */
  .brand {
    position: absolute; inset: 0;
    display: flex; align-items: center; justify-content: center; gap: 16px;
  }
  .brand__square {
    width: 34px; height: 34px; border: 4px solid var(--ink);
  }
  .brand__name {
    font-weight: 600; font-size: 58px; letter-spacing: -1px; color: var(--ink);
  }

  /* Back */
  .identity {
    position: absolute; left: 40px; top: 96px; width: 240px; text-align: right;
  }
  .identity__name {
    font-family: "Oswald", "Arial Narrow", sans-serif;
    font-weight: 600; font-size: 40px; letter-spacing: 1px;
    color: var(--accent); text-transform: uppercase; line-height: 1.1;
  }
  .identity__role { font-size: 17px; margin-top: 2px; }
  .divider {
    position: absolute; left: 306px; top: 92px; width: 2px; height: 96px;
    background: var(--accent);
  }
  .contacts {
    position: absolute; left: 330px; top: 96px; list-style: none;
    font-size: 16px; letter-spacing: .6px; line-height: 24px;
  }
  .contacts li { display: flex; align-items: center; gap: 9px; }
  .contacts svg { width: 12px; height: 12px; flex: none; color: var(--accent); }
  .address {
    position: absolute; left: 60px; bottom: 26px;
    font-size: 16px; letter-spacing: .6px;
  }
</style>
</head>
<body>
<main class="canvas">
  <section class="card card--front" aria-label="Card front">
    <div class="brand">
      <span class="brand__square" aria-hidden="true"></span>
      <span class="brand__name">Plankwell</span>
    </div>
  </section>

  <section class="card card--back" aria-label="Card back">
    <div class="identity">
      <h1 class="identity__name">Jordan Hale</h1>
      <p class="identity__role">Director</p>
    </div>
    <div class="divider"></div>
    <ul class="contacts">
      <li>
        <svg viewBox="0 0 12 12" aria-hidden="true"><path d="M3 1 L5 3.5 L4 5 Q5 7 7 8 L8.5 7 L11 9 L9.5 11 Q4 10.5 1 3 Z" fill="none" stroke="currentColor" stroke-width="1.2"/></svg>
        +330 5172-4409
      </li>
      <li>
        <svg viewBox="0 0 12 12" aria-hidden="true"><rect x="3" y="1" width="6" height="10" rx="1" fill="none" stroke="currentColor" stroke-width="1.2"/><line x1="5" y1="9" x2="7" y2="9" stroke="currentColor"/></svg>
        +330 5172-4416
      </li>
      <li>
        <svg viewBox="0 0 12 12" aria-hidden="true"><rect x="1" y="2.5" width="10" height="7" fill="none" stroke="currentColor" stroke-width="1.2"/><path d="M1 2.5 L6 6.5 L11 2.5" fill="none" stroke="currentColor" stroke-width="1.2"/></svg>
        hello@plankwell.com
      </li>
      <li>
        <svg viewBox="0 0 12 12" aria-hidden="true"><circle cx="6" cy="6" r="5" fill="none" stroke="currentColor" stroke-width="1.1"/><ellipse cx="6" cy="6" rx="2.2" ry="5" fill="none" stroke="currentColor" stroke-width="1"/><line x1="1" y1="6" x2="11" y2="6" stroke="currentColor"/></svg>
        www.plankwell.com
      </li>
    </ul>
    <p class="address">2817 Birchmont Road Dayton, OH 45409</p>
  </section>
</main>
</body>
</html>
```